Travelle Inc Catalog Designing with Modern Designing Techniques*

Catalogue of Products and Services of our company with a much modern design and with various options. we have uploaded our logo for the colors. we request you to put in your best efforts and provide us with the best designs possible. the design should be one of its class.Catalog Like Durvane Kessot Mill or KORV Steel Sweden will be nice to have. just google these companies , you will get an idea

Target Market(s)

India , Middle East and Africa

Industry/Entity Type

Steel

Colors

Designer to choose colors to be used in the design.

Requirements
Must have
• We are a Steel Company and It Should be a Modern Design
Nice to have
• Catalog Like Durvane Kessot Mill or KORV Steel Sweden

```html
<!DOCTYPE html>
<html lang="en">
<head>
<meta charset="utf-8">
<title>Travelle Inc Catalogue</title>
<link href="https://fonts.googleapis.com/css2?family=Montserrat:wght@300;400;600;700&family=Open+Sans:wght@400;600&display=swap" rel="stylesheet">
<style>
  :root{
    --bg:#e2e2e4;
    --ink:#1b1b1d;
    --ink-2:#2a2a2d;
    --red:#d3202a;
    --orange:#e8602a;
    --paper:#f3f3f4;
    --grey-text:#6d6d72;
    --light-text:#d8d8dc;
    --head:'Montserrat',sans-serif;
    --body:'Open Sans',sans-serif;
  }
  *{box-sizing:border-box;margin:0;padding:0}
  html,body{width:905px;height:1200px;overflow:hidden;background:var(--bg)}
  .canvas{width:905px;height:1200px;padding:260px 15px 0;display:grid;grid-template-columns:430px 430px;column-gap:15px;row-gap:42px;align-content:start;font-family:var(--body)}
  .spread{display:flex;width:430px;height:304px;box-shadow:0 10px 24px rgba(0,0,0,.28)}
  .page{position:relative;width:215px;height:304px;overflow:hidden}
  .page--dark{background:var(--ink);color:var(--light-text)}
  .page--light{background:var(--paper);color:var(--grey-text)}
  .photo{position:absolute}
  .footer-band{position:absolute;left:0;right:0;bottom:0;height:22px;background:var(--ink)}
  .footer-band::before{content:"";position:absolute;left:0;right:0;top:-3px;height:2px;background:linear-gradient(90deg,var(--red),var(--orange) 60%,transparent)}
  .web{position:absolute;bottom:7px;left:12px;font:400 6px var(--body);color:#bdbdc2;letter-spacing:.2px}
  .page--right .web{left:auto;right:14px}
  .tiny{font-size:4.6px;line-height:6.4px}
  .red-head{font:700 6px var(--head);color:var(--red);text-transform:uppercase;margin:6px 0 2px}

  /* cover */
  .cover-back .back-photo{left:0;top:0;width:215px;height:200px;background:radial-gradient(circle at 40% 45%,#4b3b3b,#262628 55%,var(--ink) 80%);opacity:.9}
  .cover-back .top-rule{position:absolute;left:0;top:40px;width:215px;height:2px;background:linear-gradient(90deg,transparent,var(--red) 40%,var(--orange))}
  .contact{position:absolute;left:14px;bottom:40px;width:110px;color:#a9a9ae}
  .contact .red-head{margin-top:0}
  .cover-front{background:linear-gradient(#f1f1f2 0 38px,var(--ink) 38px)}
  .brand-tab{position:absolute;right:0;top:8px;height:26px;width:110px;background:#fff;display:flex;align-items:center;gap:6px;padding-left:14px;box-shadow:0 1px 3px rgba(0,0,0,.2)}
  .brand-dot{width:11px;height:11px;border-radius:50%;background:var(--red)}
  .brand-name{font:700 11px var(--head);color:var(--red)}
  .cover-front .hero{left:0;top:42px;width:215px;height:200px;background:linear-gradient(180deg,#5a5d63 0%,#a9876a 45%,#f3b865 58%,#6a4a36 72%,#221a18 100%)}
  .plate-circles{position:absolute;left:14px;top:150px;display:flex;gap:6px}
  .plate-circles span{width:44px;height:44px;border-radius:50%;border:2px solid var(--red);background:radial-gradient(circle at 35% 35%,#d8d8da,#7b7c80)}
  .cover-title{position:absolute;left:16px;bottom:36px;color:#fff;font-family:var(--head)}
  .cover-title .line1{font-weight:600;font-size:12px}
  .cover-title .line1 em{font-style:normal;font-weight:300}
  .cover-title .line2{font-weight:700;font-size:20px;line-height:22px}

  /* about */
  .about-grid{position:absolute;left:8px;top:8px;width:199px;display:grid;grid-template-columns:1fr 1fr;grid-auto-rows:58px;gap:4px}
  .about-grid .tile{position:relative}
  .tile-plates{background:linear-gradient(135deg,#7a3a2c,#b86a4e 50%,#5b2c22)}
  .tile-stack{background:linear-gradient(135deg,#cfd0d3,#8d8f94)}
  .tile-brand{background:#111113;display:flex;align-items:center;justify-content:center;gap:5px}
  .tile-brand .brand-name{font-size:10px}
  .tile-brand .brand-dot{width:9px;height:9px}
  .tile-yard{background:linear-gradient(180deg,#b9c6d1,#777a7d)}
  .tile-sheet{background:linear-gradient(135deg,#e4e1dc,#9f9a92)}
  .tile-machine{background:linear-gradient(180deg,#9dbad4,#c6902f 60%,#5a4020)}
  .tile-port{background:linear-gradient(180deg,#a9c6df,#6f7880)}
  .about-strip{left:8px;top:14px;width:52px;height:250px;background:linear-gradient(180deg,#3a2b2a,#b7684a 45%,#f0a45f 60%,#3a2620)}
  .about-text{position:absolute;left:66px;top:14px;width:140px}
  .about-text h2{font:700 12px var(--head);color:#fff;margin-bottom:6px}
  .about-text p{color:#b9b9be}

  /* contents */
  .toc-title{position:absolute;left:18px;top:100px;transform:rotate(-90deg);transform-origin:left top;font:300 11px/12px var(--head);color:#555;letter-spacing:.5px}
  .toc-title b{font-weight:600;display:block}
  .toc-rule{position:absolute;left:44px;top:18px;width:1px;height:60px;background:var(--red)}
  .grey-block{position:absolute;left:16px;top:180px;width:60px;height:70px;background:#dcdcdf}
  .toc-box{position:absolute;left:62px;top:22px;width:153px;height:235px;background:var(--ink-2);padding:12px 12px;color:#c9c9ce}
  .toc-item{margin-bottom:12px}
  .toc-num{font:700 7px var(--head);color:var(--red)}
  .toc-head{font:600 6px var(--head);color:#fff;margin-bottom:2px}
  .furnace{left:0;top:22px;width:215px;height:110px;background:radial-gradient(circle at 55% 60%,#ffb25a,#e0531d 35%,#5a1c10 70%,#1b0f0c)}
  .contents-cols{position:absolute;left:0;top:140px;width:215px;display:grid;grid-template-columns:70px 1fr}
  .tagline{font:600 6px/8px var(--head);color:#777;text-transform:uppercase;padding:0 6px 0 12px}
  .ceo{border-left:1px solid var(--red);padding:0 10px 0 8px}
  .ceo h3{font:600 6px var(--head);color:#777;margin-bottom:3px}
  .map{left:60px;top:224px;width:155px;height:56px;background:linear-gradient(135deg,#eef0f3,#d8dde3);border-top:1px solid var(--red)}

  /* quality */
  .quality{position:relative}
  .quality-photo{left:0;top:0;width:430px;height:304px;background:linear-gradient(110deg,#1e2b45 0%,#3b5f86 35%,#6e92b8 55%,#3e6f9f 75%,#1d3150 100%)}
  .quality-copy{position:absolute;left:285px;top:26px;width:135px;color:#e6eef6}
  .quality-copy h2{font:400 13px/13px var(--head);color:#fff;letter-spacing:.5px;margin-bottom:8px}
  .quality-copy h2 span{font-weight:300;display:block}
  .strip{position:absolute;left:8px;top:214px;width:414px;height:50px;display:grid;grid-template-columns:repeat(7,1fr);gap:3px}
  .strip span:nth-child(1){background:linear-gradient(135deg,#c9ccd1,#6c7278)}
  .strip span:nth-child(2){background:linear-gradient(135deg,#7b5a3a,#d18a3a)}
  .strip span:nth-child(3){background:linear-gradient(135deg,#c86440,#5a2a1c)}
  .strip span:nth-child(4){background:linear-gradient(135deg,#6a4a2e,#b08448)}
  .strip span:nth-child(5){background:linear-gradient(135deg,#d8c4b8,#86705e)}
  .strip span:nth-child(6){background:linear-gradient(135deg,#a8b8c6,#3d5a7c)}
  .strip span:nth-child(7){background:linear-gradient(135deg,#f0b45a,#4a3a2a)}
  .quality .footer-band{height:30px}
  .quality .web-l{left:14px}
  .quality .web-r{left:auto;right:100px}
</style>
</head>
<body>
<main class="canvas">

  <section class="spread">
    <div class="page page--dark cover-back">
      <div class="photo back-photo" role="img" aria-label="Faded dark photograph of stacked steel plates"></div>
      <div class="top-rule"></div>
      <div class="contact tiny">
        <p class="red-head">Travelle Inc</p>
        <p>14 Harbour Road, Fort Area, Mumbai 400001, India. Tel +91 22 5550 0147, info@travelle.in</p>
      </div>
      <div class="footer-band"><span class="web">www.travelle.in</span></div>
    </div>
    <div class="page page--right cover-front">
      <div class="brand-tab"><span class="brand-dot"></span><span class="brand-name">Travelle</span></div>
      <div class="photo hero" role="img" aria-label="Offshore oil platform at sunset over the sea"></div>
      <div class="plate-circles" role="img" aria-label="Three circular close-ups of steel plates"><span></span><span></span><span></span></div>
      <div class="cover-title">
        <p class="line1">Solution <em>For Your</em></p>
        <p class="line2">Steel Plate</p>
      </div>
      <div class="footer-band"><span class="web">www.travelle.in</span></div>
    </div>
  </section>

  <section class="spread">
    <div class="page page--dark">
      <div class="about-grid">
        <div class="tile tile-plates" role="img" aria-label="Rusted steel plates in stacks"></div>
        <div class="tile tile-stack" role="img" aria-label="Polished steel sheets"></div>
        <div class="tile tile-brand"><span class="brand-dot"></span><span class="brand-name">Travelle</span></div>
        <div class="tile tile-sheet" role="img" aria-label="Close-up of a steel plate surface"></div>
        <div class="tile tile-yard" role="img" aria-label="Steel yard with plates on the ground"></div>
        <div class="tile tile-stack" role="img" aria-label="Steel plates laid out in a warehouse"></div>
        <div class="tile tile-machine" role="img" aria-label="Large industrial gear machinery"></div>
        <div class="tile tile-port" role="img" aria-label="Industrial harbour with cranes"></div>
      </div>
      <div class="footer-band"><span class="web">www.travelle.in</span></div>
    </div>
    <div class="page page--dark page--right">
      <div class="photo about-strip" role="img" aria-label="Pier structure against a setting sun"></div>
      <div class="about-text">
        <h2>About Travelle</h2>
        <p class="tiny">We are a professionally managed steel plate company, supplying carbon, alloy, boiler, offshore and wear resistant plates. Our team holds a large stock and works closely with mills to deliver on time to every client across many markets.</p>
        <p class="red-head">Services</p>
        <p class="tiny">We offer value added services such as cutting, testing and inspection, so our clients receive plates ready for use with short lead times.</p>
        <p class="red-head">Quality</p>
        <p class="tiny">Being an ISO certified company, we follow strict quality rules. Every plate comes with mill test certificates and full traceability on request.</p>
      </div>
      <div class="footer-band"><span class="web">www.travelle.in</span></div>
    </div>
  </section>

  <section class="spread">
    <div class="page page--light">
      <div class="toc-rule"></div>
      <h2 class="toc-title">TABLE OF<b>CONTENTS</b></h2>
      <div class="grey-block"></div>
      <div class="toc-box">
        <div class="toc-item"><p class="toc-num">02</p><p class="toc-head">Headline One</p><p class="tiny">Short summary of the section and its key points here.</p></div>
        <div class="toc-item"><p class="toc-num">04</p><p class="toc-head">Headline One</p><p class="tiny">Short summary of the section and its key points here.</p></div>
        <div class="toc-item"><p class="toc-num">08</p><p class="toc-head">Headline One</p><p class="tiny">Short summary of the section and its key points here.</p></div>
        <div class="toc-item"><p class="toc-num">12</p><p class="toc-head">Headline One</p><p class="tiny">Short summary of the section and its key points here.</p></div>
        <div class="toc-item"><p class="toc-num">16</p><p class="toc-head">Headline One</p><p class="tiny">Short summary of the section and its key points here.</p></div>
      </div>
      <div class="footer-band"><span class="web">www.travelle.in</span></div>
    </div>
    <div class="page page--light page--right">
      <div class="photo furnace" role="img" aria-label="Worker silhouetted against a glowing steel furnace"></div>
      <div class="contents-cols">
        <p class="tagline">Steel plates distributor, stockholder and supplier in India, Singapore, Middle East &amp; Europe</p>
        <div class="ceo">
          <h3>CEO &amp; FOUNDER</h3>
          <p class="tiny">Our founder built the company on trust, fair pricing and fast delivery. Today we serve clients in many countries and keep growing our stock.</p>
        </div>
      </div>
      <div class="photo map" role="img" aria-label="Map showing office and warehouse locations"></div>
      <div class="footer-band"><span class="web">www.travelle.in</span></div>
    </div>
  </section>

  <section class="spread quality">
    <div class="photo quality-photo" role="img" aria-label="Steel plant towers and rusty pipes under a blue sky"></div>
    <div class="quality-copy">
      <h2>QUALITY<span>POLICY</span></h2>
      <p class="tiny">We are committed to furnish superior quality products at a reasonable price with schedule. It is our endeavour to follow the principles of total quality management. Our quality system has been certified and we keep improving our processes, testing and service to meet every client need.</p>
    </div>
    <div class="strip" role="img" aria-label="Row of photos: refinery pipes, worker, steel coils, machinery, welder, steel mill">
      <span></span><span></span><span></span><span></span><span></span><span></span><span></span>
    </div>
    <div class="footer-band"><span class="web web-l">www.travelle.in</span><span class="web web-r">www.travelle.in</span></div>
  </section>

</main>
</body>
</html>
```